Ridgeway Marksman Range wordpress theme

I want a Wordpress theme that is classy, unusual, colorful, etc. based on my attached logo files.

Font:
- Serpentine-Bold-Bold for "RIDGEWAY"
- BrowalliaUPC for "MARKSMAN RANGE"

Colors (CMYK code):
- BLACK ....... 0; 0; 0; 100;
- ORANGE ... gradient from 0; 65; 97.5; 0 to 0; 39; 97.5; 0

```html
<!DOCTYPE html>
<html lang="en">
<head>
<meta charset="utf-8">
<title>Ridgeway Marksman Range</title>
<link rel="stylesheet" href="https://fonts.googleapis.com/css2?family=Open+Sans:wght@400;600;700&family=Oswald:wght@500&family=Orbitron:wght@700&family=Arimo&display=swap">
<style>
:root{
  --orange:#ee8a1c;
  --orange-deep:#e06a12;
  --orange-text:#ee7a16;
  --black:#151515;
  --nav:#1b1b1b;
  --panel:#f7f7f7;
  --body-text:#3a3a3a;
  --footer:#242424;
  --footer-text:#c9c9c9;
}
*{margin:0;padding:0;box-sizing:border-box}
html,body{width:920px;height:1200px;overflow:hidden}
body{position:relative;background:linear-gradient(180deg,#8a4a10 0,#b2661a 260px,#d9a46a 400px,#ececec 480px,#ececec 100%);font-family:"Open Sans",sans-serif}
.page{position:absolute;left:78px;top:0;width:764px;height:992px;background:linear-gradient(180deg,#e6e6e6 0,#f9f9f9 200px,#f6f6f6 100%)}
.social{position:absolute;left:99px;top:36px;display:flex;gap:7px}
.social span{width:26px;height:26px;border-radius:50%;background:#555;display:flex;align-items:center;justify-content:center}
.social span.alt{background:var(--orange)}
.top-phone{position:absolute;right:92px;top:38px;display:flex;align-items:center;gap:8px;font-size:16px;color:#444;white-space:nowrap}
.nav{position:absolute;left:94px;top:85px;width:736px;height:41px;background:var(--nav);border-radius:20px}
.nav a{position:absolute;top:11px;font-family:"Oswald",sans-serif;font-size:13.5px;color:#fff;text-decoration:none;letter-spacing:.2px}
.brand{position:absolute;left:384px;top:44px;width:140px;display:flex;flex-direction:column;align-items:center;gap:14px}
.brand .dot{width:34px;height:34px;border-radius:50%;background:var(--orange)}
.brand p{font-weight:700;font-size:11px;line-height:13px;color:#fff;text-align:center;white-space:nowrap}
.hero{position:absolute;left:94px;top:132px;width:732px;height:306px;background:linear-gradient(120deg,#5a6b3a 0,#3f4a2e 40%,#2b2b2b 60%,#7b7a6e 100%)}
.hero-caption{position:absolute;left:376px;top:47px;width:356px;height:40px;background:rgba(60,60,60,.75);font-family:"Orbitron",sans-serif;font-weight:700;font-size:17px;color:#fff;letter-spacing:1px;display:flex;align-items:center;justify-content:center;white-space:nowrap}
.section-title{position:absolute;left:87px;top:470px;width:746px;display:flex;align-items:center;gap:14px}
.section-title hr{flex:1;border:0;border-top:1px solid #c8c8c8}
.section-title h2{font-size:25px;font-weight:600;color:var(--orange-text);letter-spacing:.5px}
.intro{position:absolute;left:94px;top:508px;width:732px;font-family:"Arimo",sans-serif;font-size:11.5px;line-height:17px;color:var(--body-text);text-align:center}
.intro p+p{margin-top:13px}
.more{position:absolute;left:406px;top:652px;width:96px;height:36px;background:#3a3a3a;border-radius:48px 48px 0 0;color:#fff;font-size:10.5px;font-weight:600;text-align:center;padding-top:17px}
.divider{position:absolute;left:160px;top:688px;width:600px;height:1px;background:linear-gradient(90deg,transparent,#cfcfcf,transparent)}
.card{position:absolute;top:736px;width:216px;height:222px}
.card .frame{position:absolute;left:6px;top:0;width:210px;height:222px;background:#fff;box-shadow:0 2px 5px rgba(0,0,0,.18)}
.card h3{position:absolute;left:0;top:10px;width:222px;height:42px;background:linear-gradient(180deg,var(--orange),var(--orange-deep));color:#fff;font-size:18px;font-weight:600;padding:8px 0 0 23px;box-shadow:0 2px 3px rgba(0,0,0,.2);white-space:nowrap}
.card .photo{position:absolute;left:14px;top:52px;width:194px;height:158px}
.card .photo span{position:absolute;left:0;bottom:0;width:100%;height:31px;background:rgba(30,30,30,.8);color:#fff;font-size:11.5px;padding:7px 0 0 8px}
.footer{position:absolute;left:0;top:992px;width:920px;height:208px;background:linear-gradient(180deg,#2a2a2a,#1d1d1d);color:var(--footer-text)}
.foot-brand{position:absolute;left:99px;top:32px;width:150px;height:100px;display:flex;flex-direction:column;align-items:center;justify-content:center;gap:10px}
.foot-brand .dot{width:30px;height:30px;background:var(--orange);border-radius:50%}
.foot-brand p{font-weight:700;font-size:12px;line-height:15px;color:var(--orange);text-align:center;white-space:nowrap}
.copy{position:absolute;left:86px;top:148px;width:180px;font-size:9.5px;line-height:15px;text-align:center}
.address{position:absolute;left:305px;top:26px;font-size:11px;line-height:21px;text-align:center;display:flex;gap:18px}
.address div+div{border-left:1px solid #3c3c3c;padding-left:18px}
.map{position:absolute;left:309px;top:78px;width:234px;height:113px;background:linear-gradient(135deg,#cfc8b4,#bdb59d);border:2px solid #e2e2e2}
.contact{position:absolute;left:612px;top:26px;width:240px}
.contact h4{font-size:13px;font-weight:400;color:#d8d8d8;white-space:nowrap}
.contact .line{display:flex;align-items:center;gap:12px;margin-left:10px}
.contact .phone{margin-top:16px;font-size:17px}
.contact .mail{margin-top:11px;font-size:11.5px;margin-left:6px}
.contact hr{border:0;border-top:1px solid #3e3e3e;margin:14px 0 0 14px;width:200px}
.foot-social{display:flex;gap:11px;margin:11px 0 0 48px}
.foot-social span{width:20px;height:20px;border-radius:50%;background:#4a4a4a}
.blog{font-size:11.5px;margin-top:7px;margin-left:2px}
</style>
</head>
<body>
<div class="page"></div>

<div class="social">
  <span></span><span></span><span class="alt"></span>
  <span><svg width="12" height="9" viewBox="0 0 12 9"><rect x=".5" y=".5" width="11" height="8" fill="none" stroke="#fff"/><path d="M.5 .5 6 5 11.5 .5" fill="none" stroke="#fff"/></svg></span>
</div>

<div class="top-phone">
  <svg width="24" height="24" viewBox="0 0 24 24"><circle cx="12" cy="12" r="11" fill="none" stroke="#ee8a1c" stroke-width="1.6"/><path d="M8 6c1 0 2 2 2 3s-1 1-1 2 3 4 4 4 1-1 2-1 3 1 3 2-1 2-2 2C11 18 6 12 6 8c0-1 1-2 2-2z" fill="#ee8a1c"/></svg>
  <span>+44 (0)1632 960418</span>
</div>

<nav class="nav">
  <a style="left:33px">HOME</a>
  <a style="left:104px">ABOUT US</a>
  <a style="left:194px">SERVICES &amp; FAQ</a>
  <a style="left:444px">MEMBERSHIP</a>
  <a style="left:544px">CLASSES &amp; EVENTS</a>
  <a style="left:672px">CONTACT</a>
</nav>

<div class="brand">
  <span class="dot"></span>
  <p>RIDGEWAY<br>MARKSMAN RANGE</p>
</div>

<div class="hero" role="img" aria-label="Photo of a shooter aiming a shotgun at an outdoor range">
  <div class="hero-caption">RIDGEWAY MARKSMAN RANGE</div>
</div>

<div class="section-title"><hr><h2>WHO WE ARE</h2><hr></div>

<div class="intro">
  <p>Our experienced public relations specialists bring together a wealth of experience in public relations (PR), market research, magazines, FMCG / food and beverage marketing, television, and editorial journalism. We help our clients get closer to the mind of their target customer than they have ever been before.</p>
  <p>At Summit PR, our marketing &amp; communications experts will work closely with you as your New Zealand public relations firm and if required, even as your advertising agency. Unlike many other public relations companies we also plan and buy media – however one of our key points of difference is our ability to enhance your brand equity by integrating your TV, print or digital marketing spend with an effective public relations strategy. Whether you are a small independent retailer or a large multinational corporation.</p>
</div>

<div class="more">More Details</div>
<div class="divider"></div>

<div class="card" style="left:91px">
  <div class="frame"></div>
  <h3>Training Courses</h3>
  <div class="photo" role="img" aria-label="Photo of an instructor and student shooting clays" style="background:linear-gradient(135deg,#c98a3a,#6d5a3a)"><span>Simply dummy text the printing</span></div>
</div>
<div class="card" style="left:349px">
  <div class="frame"></div>
  <h3>Guns &amp; Equipment</h3>
  <div class="photo" role="img" aria-label="Photo of a revolver and cartridges on a target" style="background:linear-gradient(135deg,#6a6a66,#1e1e1e)"><span>Simply dummy text the printing</span></div>
</div>
<div class="card" style="left:603px">
  <div class="frame"></div>
  <h3>Events &amp; Competitions</h3>
  <div class="photo" role="img" aria-label="Photo of two competitors at an indoor range event" style="background:linear-gradient(135deg,#8e8e8a,#6a3c34)"><span>Simply dummy text the printing</span></div>
</div>

<footer class="footer">
  <div class="foot-brand"><span class="dot"></span><p>RIDGEWAY<br>MARKSMAN RANGE</p></div>
  <div class="copy">© 2012 ridgewaymarksmanrange<br>All Rights Reserved</div>
  <div class="address">
    <div>1480 Ridgeway Rd<br>Jackson, TN 38305</div>
    <div>Mon - Sat 9am - 8pm<br>Sunday 11am - 6pm</div>
  </div>
  <div class="map" role="img" aria-label="Street map showing the range location"></div>
  <div class="contact">
    <h4>Contact Ridgeway Marksman Range</h4>
    <div class="line phone">
      <svg width="20" height="14" viewBox="0 0 20 14"><path d="M1 5C1 2 6 1 10 1s9 1 9 4l-4 1-1-2H6L5 6z" fill="#e07a1a"/><rect x="5" y="7" width="10" height="6" rx="1" fill="#e07a1a"/></svg>
      <span>615 - 555 - 0142</span>
    </div>
    <div class="line mail">
      <svg width="20" height="13" viewBox="0 0 20 13"><rect width="20" height="13" fill="#e07a1a"/><path d="M0 0 10 7 20 0" fill="none" stroke="#242424" stroke-width="1.4"/></svg>
      <span>info@ridgewayrange.com</span>
    </div>
    <hr>
    <div class="foot-social"><span></span><span></span><span></span></div>
    <div class="blog">Ridgeway Marksman Range Blog</div>
  </div>
</footer>
</body>
</html>
```